Engineering Land Development Company Needs Flyer Brochure for Prospective Professional Clients

Our company provides land development site design for commercial projects. We have many repeat clients that are familiar with our work. We do not advertise our services other than a website. Most of our referrals are from existing clients. When a new client contacts us and asks for a proposal for a project we would like to have a brochure that shows our strengths, experience, and professionalism. We are selling professional services similar to a lawyer or accountant. We want new clients to feel comfortable hiring a new firm. The brochure would be one page single-side included when we submit proposals for new projects. Check out our website at tovarnix.com for more info. We would like a brochure that mixes grading/excavation construction work on a job site with business professional. We will need to update the brochure so we want it in .doc .psd or some other edit format. The brochure we are using is attached. It is very two-dimensional. We need some depth.

Target Market(s)

Land developers, architects, real estate, professionals, attorneys

Industry/Entity Type

Real Estate Development

Font styles to use
Sans Serif
Other font styles liked:
• calibri

Colors
0355a3
9bcb3c

Requirements
Must have
• company logo, ability to update text and images
Nice to have
• background image(s) with text overlay
Should not have
• cartoons, harsh colors, stock photos of people, lots of boxes

```html
<!DOCTYPE html>
<html lang="en">
<head>
<meta charset="utf-8">
<title>Tovarnix Engineering – Land Development Flyer</title>
<link rel="stylesheet" href="https://fonts.googleapis.com/css2?family=Roboto+Condensed:ital,wght@0,400;0,700;1,400;1,700&family=Lato:wght@400;700&family=Merriweather:wght@300&display=swap">
<style>
  :root{
    --brand-blue:#5557a6;
    --brand-green:#7dc143;
    --text-dark:#2f2f38;
    --icon-grey:#8d8d8f;
    --stage-bg:#2b2b2d;
    --photo-dark:#7a6350;
    --photo-light:#d9cbbb;
  }
  *{box-sizing:border-box;margin:0;padding:0}
  html,body{width:1200px;height:1200px;overflow:hidden;background:var(--stage-bg)}
  .flyer{position:absolute;left:170px;top:45px;width:860px;height:1110px;background:linear-gradient(180deg,#f4f4f6 0%,#ffffff 40%,#f1f1f3 100%);overflow:hidden;font-family:"Roboto Condensed",sans-serif}
  .header-art{position:absolute;left:0;top:0}
  .brand{position:absolute;left:40px;top:40px}
  .brand-mark{width:78px;height:78px;background:var(--brand-blue);margin:0 0 16px 20px}
  .brand-name{font-family:"Merriweather",serif;font-weight:300;font-size:17px;color:var(--brand-blue);display:flex;align-items:center;gap:8px}
  .brand-name::before{content:"";width:14px;height:14px;background:var(--brand-blue)}
  .mission{position:absolute;left:40px;top:254px;font-weight:700;font-size:28px;line-height:33px;text-transform:uppercase}
  .mission .g{color:var(--brand-green)} .mission .b{color:var(--brand-blue)}
  .intro{position:absolute;left:40px;top:394px;width:660px;font-size:16px;line-height:21px;color:var(--brand-blue);font-weight:700;font-style:italic}
  .rule{position:absolute;height:2px;background:var(--brand-blue)}
  .rule::after{content:"";position:absolute;right:-6px;top:-5px;width:12px;height:12px;border-radius:50%;background:var(--brand-blue)}
  .service{position:absolute;left:0;width:860px}
  .service-icon{position:absolute;left:60px;top:4px;width:130px;text-align:center}
  .service-icon svg{display:block;margin:0 auto 4px}
  .service-label{font-size:14px;color:var(--brand-green);font-weight:700;text-transform:uppercase}
  .service-text{position:absolute;left:225px;top:0;width:605px}
  .service-text h2{font-size:18px;line-height:20px;color:var(--brand-green);font-weight:700;margin-bottom:4px}
  .service-text p{font-family:"Lato",sans-serif;font-size:12px;line-height:16px;color:var(--text-dark);font-weight:700}
  .clients-band{position:absolute;right:0;top:968px;width:530px;height:42px;background:var(--brand-blue);clip-path:polygon(7% 0,100% 0,100% 100%,0 100%);color:#fff;font-style:italic;font-size:14px;line-height:17px;padding:4px 16px 0 60px;text-align:right}
  .clients{position:absolute;left:460px;top:1020px;width:390px;display:grid;grid-template-columns:repeat(4,1fr);gap:6px 6px}
  .client{font-weight:700;font-size:11px;line-height:14px;color:var(--brand-blue);display:flex;align-items:center;gap:4px;white-space:nowrap}
  .client::before{content:"";width:7px;height:7px;border-radius:50%;background:var(--brand-blue);flex:none}
  .contact-top{position:absolute;left:0;top:1006px;width:440px;height:2px;background:var(--brand-blue)}
  .contact{position:absolute;left:0;top:1014px;width:450px;height:96px;background:var(--brand-blue);clip-path:polygon(0 0,80% 0,100% 100%,0 100%);color:#fff;font-size:16px;font-weight:700;line-height:21px;padding:6px 0 0 40px;font-style:normal}
  .contact-row{display:flex;align-items:center;gap:12px}
  .contact-row svg{flex:none}
</style>
</head>
<body>
<main class="flyer">
  <svg class="header-art" width="860" height="420" viewBox="0 0 860 420">
    <defs>
      <linearGradient id="photoTone" x1="0" y1="0" x2="1" y2="1">
        <stop offset="0" stop-color="var(--photo-light)"/>
        <stop offset="0.55" stop-color="#a58c75"/>
        <stop offset="1" stop-color="var(--photo-dark)"/>
      </linearGradient>
      <linearGradient id="swoosh" x1="0" y1="0" x2="1" y2="0">
        <stop offset="0" stop-color="#5e9c2c"/>
        <stop offset="0.5" stop-color="var(--brand-green)"/>
        <stop offset="1" stop-color="#a6d86a"/>
      </linearGradient>
    </defs>
    <path role="img" aria-label="Sepia photo of two engineers in hard hats reviewing plans beside large industrial gears" d="M300,0 H860 V210 C820,240 790,300 760,385 C700,300 600,210 480,190 C420,180 360,190 300,200 Z" fill="url(#photoTone)"/>
    <path d="M0,225 C160,175 360,150 480,172 C610,195 710,290 760,385 C790,300 820,240 860,205 V222 C825,250 795,320 760,410 C705,315 610,215 480,195 C360,175 170,200 0,245 Z" fill="url(#swoosh)"/>
  </svg>

  <div class="brand">
    <div class="brand-mark"></div>
    <div class="brand-name">Tovarnix Engineering PLLC</div>
  </div>

  <h1 class="mission">
    <span class="g">Our mission at Tovarnix</span><br>
    <span class="b">Engineering is to provide</span><br>
    <span class="g">superior quality</span> <span class="b">professional</span><br>
    <span class="b">land development services</span>
  </h1>

  <p class="intro">Our firm provides planning, surveying, engineering, and environmental services which allows us to focus on the entire land development process rather than one specific discipline. Providing a broad scope of professional services helps to streamline a project by eliminating many disadvantages of having multiple firms with overlapping responsibilities.</p>

  <div class="rule" style="left:40px;top:486px;width:540px"></div>

  <article class="service" style="top:498px">
    <div class="service-icon">
      <svg width="60" height="60" viewBox="0 0 70 70"><circle cx="35" cy="35" r="32" fill="none" stroke="var(--icon-grey)" stroke-width="5"/><rect x="23" y="18" width="24" height="32" rx="2" fill="none" stroke="var(--icon-grey)" stroke-width="3"/><path d="M27 28l3 3 5-5M27 40l3 3 5-5" fill="none" stroke="var(--icon-grey)" stroke-width="2.5"/><path d="M38 30h6M38 42h6" stroke="var(--icon-grey)" stroke-width="2.5"/></svg>
      <div class="service-label">Planning</div>
    </div>
    <div class="service-text">
      <h2>We are land development professionals who can see the “big picture”.</h2>
      <p>We have extensive experience with site selection, due diligence investigations, re-zonings, and land planning. Every project is different. We look forward to identifying all feasible alternatives. We become part of the project and enjoy developing the best plan for the success of each particular project. We understand that time is money and unexpected delays are unacceptable.</p>
    </div>
  </article>
  <div class="rule" style="left:225px;top:594px;width:380px"></div>

  <article class="service" style="top:604px">
    <div class="service-icon">
      <svg width="60" height="60" viewBox="0 0 70 70"><circle cx="35" cy="35" r="34" fill="var(--icon-grey)"/><circle cx="35" cy="20" r="4" fill="none" stroke="#fff" stroke-width="2.5"/><path d="M33 24L23 52M37 24l10 28M26 40h18" stroke="#fff" stroke-width="2.5" fill="none"/></svg>
      <div class="service-label">Surveying</div>
    </div>
    <div class="service-text">
      <h2>We are land development professionals who provide superior quality surveying services.</h2>
      <p>We have extensive experience with site selection, due diligence investigations, re-zonings, and land planning. Every project is different. We look forward to identifying all feasible alternatives. We become part of the project and enjoy developing the best plan for the success of each particular project.</p>
    </div>
  </article>
  <div class="rule" style="left:225px;top:722px;width:270px"></div>

  <article class="service" style="top:732px">
    <div class="service-icon">
      <svg width="60" height="60" viewBox="0 0 70 70"><circle cx="35" cy="35" r="34" fill="var(--icon-grey)"/><path d="M44 22a9 9 0 0 0-11 11L20 46l4 4 13-13a9 9 0 0 0 11-11l-5 5-4-1-1-4z" fill="#fff"/></svg>
      <div class="service-label">Engineering</div>
    </div>
    <div class="service-text">
      <h2>We are land development professionals who can handle the most complicated engineering challenge.</h2>
      <p>Let us worry about all the technical stuff and the regulators. Our firm has extensive experience with infrastructure assessments, erosion control, grading, roadway design, stormwater management, water systems, sewer systems, utilities, flood plain management, landscape design, permitting, bidding, and construction administration.</p>
    </div>
  </article>
  <div class="rule" style="left:510px;top:850px;width:310px"></div>

  <article class="service" style="top:860px">
    <div class="service-icon">
      <svg width="60" height="60" viewBox="0 0 70 70"><circle cx="35" cy="35" r="34" fill="var(--icon-grey)"/><path d="M22 50C20 34 32 20 50 20c0 18-12 30-28 30z" fill="#fff"/><path d="M22 50L42 28" stroke="var(--icon-grey)" stroke-width="2.5"/></svg>
      <div class="service-label">Environmental</div>
    </div>
    <div class="service-text">
      <h2>We are land development professionals who provide superior quality environmental services.</h2>
      <p>We provide environmental site assessments, underground storage tank management, soil and groundwater sampling and testing, contamination remediation, Brownfields assessments, permitting and redevelopment, and wetlands permitting. Our firm works closely with state and federal agencies to provide economical mitigation and remediation solutions.</p>
    </div>
  </article>

  <div class="clients-band">Our business would not be successful without the support of our clients.<br>Some of our project clients include :</div>
  <div class="clients">
    <span class="client">Harlan Home</span><span class="client">Kestrel Motors</span><span class="client">Lumora Tel</span><span class="client">Brookfarm Foods</span>
    <span class="client">Maple Griddle</span><span class="client">Casa Vero</span><span class="client">Crustline</span><span class="client">Pistonwell Auto</span>
    <span class="client">Fieldmark Tractor</span><span class="client">Salsa Bay</span><span class="client">Greenleaf Grocer</span><span class="client">Pawsly</span>
    <span class="client">Roastery Nine</span><span class="client">Burrito Row</span><span class="client">Wingfield Grill</span><span class="client">Ruby's Burgers</span>
  </div>

  <div class="contact-top"></div>
  <address class="contact">
    <div class="contact-row"><svg width="16" height="16" viewBox="0 0 16 16"><path d="M8 1L1 8h2v7h4v-4h2v4h4V8h2z" fill="#fff"/></svg><span>418 Alder Street – Suite 300 West<br>Carverton, NC 28740</span></div>
    <div class="contact-row"><svg width="16" height="16" viewBox="0 0 16 16"><path d="M3 1l3 3-2 2c1 2 3 4 5 5l2-2 3 3-2 3C6 14 2 10 1 3z" fill="#fff"/></svg><span>(555) 014-2790</span></div>
    <div class="contact-row"><svg width="16" height="16" viewBox="0 0 16 16"><circle cx="8" cy="8" r="6.5" fill="none" stroke="#fff" stroke-width="1.5"/><path d="M1.5 8h13M8 1.5c-3 3-3 10 0 13M8 1.5c3 3 3 10 0 13" fill="none" stroke="#fff" stroke-width="1.2"/></svg><span>www.tovarnix.com</span></div>
  </address>
</main>
</body>
</html>
```